Utility Software Company Needs a Business Flyer

We need a business flyer to promote one of our Services. The MBA Department is a Service within our company and it is basically Managed Backoffice Administration. MBA provides services that lighten the workload for our clients. MBA has a team of professionals who specialize in data processing, bill processing, research, customer support, and security of financial data. We remove the burden of in house billing and payment processing.

Target Market(s)

New and existing utility customers

Industry/Entity Type

Public Utility

Font styles to use
Serif

Colors
ffcf3e
3277b5
85cae6

Requirements
Must have
• The company name - KLT, Inc.
• Logo
• Tagline
• Address - 48715 Brisbow Lane, Houston, TX 77052
• Phone: 713-846-2957
• Email: sales@kltqe.example
• Website - www.kltqe.example
• Contact a Sales Associate for more information
• Diverse images of people

```html
<!DOCTYPE html>
<html lang="en">
<head>
<meta charset="utf-8">
<title>KLT, Inc. – MBA Data Processing Flyer</title>
<link rel="stylesheet" href="https://fonts.googleapis.com/css2?family=Montserrat:wght@300;400;500;600;700;800;900&display=swap">
<style>
:root{
  --navy:#0b3c7d;
  --navy-deep:#082c5e;
  --blue:#1f5aa6;
  --sky:#2f9ad8;
  --sky-light:#4cb3e6;
  --gold:#f6b93b;
  --text:#4a4f57;
  --white:#ffffff;
  --stage:#d9d9d9;
}
*{margin:0;padding:0;box-sizing:border-box}
html,body{width:1200px;height:1200px;overflow:hidden;background:var(--stage)}
body{font-family:"Montserrat",sans-serif;color:var(--text)}
.stage{position:absolute;left:0;top:0;width:1500px;height:1500px;transform:scale(.8);transform-origin:0 0}
.page{position:absolute;top:230px;width:638px;height:895px;background:var(--white);overflow:hidden}
.page--front{left:83px}
.page--back{left:793px}
.abs{position:absolute}
.bottom-bar{left:0;bottom:0;width:100%;height:11px;background:var(--navy)}

/* front */
.hero-band{left:0;top:0;width:100%;height:310px;background:linear-gradient(120deg,var(--navy-deep),var(--blue) 70%,#2d6fbd)}
.hero-photo{left:279px;top:36px;width:349px;height:424px;background:linear-gradient(150deg,#e7eef6 0%,#b9c8da 40%,#5b6f8c 75%,#2b3a52 100%)}
.accent-line{left:259px;top:280px;width:6px;height:180px;background:var(--gold)}
.title-main{left:26px;top:40px;font-size:66px;font-weight:900;color:var(--white);letter-spacing:2px;line-height:1}
.title-sub{left:27px;top:112px;font-size:30px;font-weight:800;color:var(--gold);letter-spacing:1px}
.title-amp{left:26px;top:148px;font-size:33px;font-weight:400;color:var(--white)}
.hero-tagline{left:26px;top:200px;width:200px;font-size:15.5px;color:var(--white);line-height:1.2}
.brand{left:28px;top:360px;display:flex;align-items:center;gap:12px}
.brand-dot{width:28px;height:28px;border-radius:50%;background:var(--gold)}
.brand-name{font-size:54px;font-weight:800;color:var(--blue);letter-spacing:1px}
.intro-title{left:19px;top:495px;width:610px;font-size:14.5px;font-weight:600;color:var(--navy);line-height:1.2}
.intro-body{left:19px;top:539px;width:602px;font-size:9.6px;line-height:1.32;text-align:justify}
.intro-body p{margin-bottom:11px}
.contact-rule{left:43px;top:740px;width:2px;height:100px;background:var(--gold)}
.contact{left:25px;display:flex;align-items:flex-start;gap:16px;font-size:13px;font-weight:500;color:#222}
.contact svg{width:12px;height:12px;flex:none;margin-top:2px}
.signoff{left:245px;top:826px;display:flex;align-items:center;gap:10px}
.signoff-name{font-size:28px;font-weight:800;color:var(--blue)}
.signoff-tag{font-size:19px;font-weight:700;color:var(--navy)}

/* back */
.section-title{left:18px;font-size:18.5px;font-weight:700;color:var(--navy)}
.section-rule{left:18px;width:138px;height:3px;background:var(--gold)}
.lead{left:19px;top:57px;font-size:9.6px}
.sub-title{left:18px;top:110px;font-size:14px;font-weight:700;color:var(--navy)}
.service{left:24px;width:600px;display:flex;font-size:9.8px;line-height:1.3}
.service-name{width:104px;flex:none;font-size:12.5px;font-weight:600;color:var(--blue);line-height:1.2;padding-left:12px;position:relative}
.service-name::before{content:"";position:absolute;left:0;top:5px;width:4px;height:4px;border-radius:50%;background:var(--navy)}
.service-desc{flex:1}
.advantages{left:18px;top:556px;width:601px;height:260px;background:linear-gradient(135deg,var(--sky) 0%,var(--sky-light) 50%,var(--sky) 100%);color:var(--white);font-size:10.2px;line-height:1.25}
.adv-divider{left:299px;top:14px;width:2px;height:228px;background:var(--white)}
.adv-list{position:absolute;top:22px;list-style:none}
.adv-list li{display:flex;gap:6px}
.adv-list .num{color:var(--gold);font-weight:700;width:12px;flex:none}
.adv-list ul{list-style:disc;padding-left:16px;margin-top:8px}
.adv-list ul li{display:list-item;margin-bottom:2px}
.back-footer{left:36px;top:846px;display:flex;gap:24px;font-size:12.5px;font-weight:500;color:#222}
.back-footer span{display:flex;align-items:center;gap:9px}
.back-footer svg{width:11px;height:11px}
</style>
</head>
<body>
<svg width="0" height="0" style="position:absolute">
  <defs>
    <symbol id="icon-phone" viewBox="0 0 24 24"><path fill="#1f5aa6" d="M6.6 10.8a15.1 15.1 0 0 0 6.6 6.6l2.2-2.2a1 1 0 0 1 1-.25 11.4 11.4 0 0 0 3.6.57 1 1 0 0 1 1 1V20a1 1 0 0 1-1 1A17 17 0 0 1 3 4a1 1 0 0 1 1-1h3.5a1 1 0 0 1 1 1c0 1.250.2 2.450.57 3.57a1 1 0 0 1-.25 1z"/></symbol>
    <symbol id="icon-globe" viewBox="0 0 24 24"><circle cx="12" cy="12" r="9" fill="none" stroke="#1f5aa6" stroke-width="2.4"/><path d="M3 12h18M12 3c3 3 3 15 0 18M12 3c-3 3-3 15 0 18" fill="none" stroke="#1f5aa6" stroke-width="1.8"/></symbol>
    <symbol id="icon-pin" viewBox="0 0 24 24"><path fill="#1f5aa6" d="M12 2a7 7 0 0 0-7 7c0 5.2 7 13 7 13s7-7.8 7-13a7 7 0 0 0-7-7zm0 9.5A2.5 2.5 0 1 1 12 6.5a2.5 2.5 0 0 1 0 5z"/></symbol>
  </defs>
</svg>

<div class="stage">
  <!-- FRONT -->
  <section class="page page--front">
    <div class="abs hero-band"></div>
    <div class="abs hero-photo" role="img" aria-label="Photo of two smiling businessmen in suits reviewing documents and a tablet at a desk"></div>
    <div class="abs accent-line"></div>
    <h1 class="abs title-main">DATA</h1>
    <div class="abs title-sub">PROCESSING</div>
    <div class="abs title-amp">&amp; Posting</div>
    <p class="abs hero-tagline">Helping to streamline your back office to manage work more efficiently.</p>

    <div class="abs brand"><span class="brand-dot"></span><span class="brand-name">KLT</span></div>

    <h2 class="abs intro-title">Data Processing &amp; Bill Processing – Managed Backoffice Administration, Services That Lighten Your Work Load</h2>
    <div class="abs intro-body">
      <p>The KLT Managed Backoffice Administration (MBA) is here to help you manage your business effectively by systematically organizing your data and information from diverse sources, allowing you and your staff/teams to spend more time serving your customers. We convert, enter, manage, evaluate and process your data based on the individual municipality rate ordinance or per your requirement(s). With a wide range of services, we have helped companies streamline their back office and manage work more efficiently. You can rely on our extensive industry knowledge and flexible services that are cost-effective and productive</p>
      <p>We have an efficient and experienced team working with a vast understanding of the various tasks involved in completing the entire billing cycle. All our representatives are friendly and knowledgeable. KLT will methodically maintain all the records and data for you, conducting processes for better client and customer relationships, bringing you maximum value.</p>
      <p>We provide you with total transparency of data. If required, we inter-connect your data so that it is easily available to your staff immediately, making interacting with customers more convenient.</p>
    </div>

    <div class="abs contact-rule"></div>
    <div class="abs contact" style="top:750px"><svg><use href="#icon-phone"/></svg><span>855.412.0937</span></div>
    <div class="abs contact" style="top:773px"><svg><use href="#icon-globe"/></svg><span>www.kltqe.example</span></div>
    <div class="abs contact" style="top:803px"><svg><use href="#icon-pin"/></svg><span>48715 Brisbow Lane<br>Houston, TX 77052</span></div>

    <div class="abs signoff"><span class="signoff-name">KLT</span><span class="signoff-tag">Dependable Utility Services</span></div>
    <div class="abs bottom-bar"></div>
  </section>

  <!-- BACK -->
  <section class="page page--back">
    <h2 class="abs section-title" style="top:18px">Services MBA provides:</h2>
    <div class="abs section-rule" style="top:46px"></div>
    <p class="abs lead">Payment channels that MBA processes:</p>

    <div class="abs service" style="top:76px"><div class="service-name">kScan</div><div class="service-desc">Lock Box – Payments that are mailed to a secure mail box and processed in the MBA office daily Monday – Friday.&nbsp; All payments received each day are processed the same day.</div></div>

    <h3 class="abs sub-title">Online Payments</h3>

    <div class="abs service" style="top:135px"><div class="service-name">SwiftRemit</div><div class="service-desc">Payments made using the QR Code on the customer’s billing statement which allows the customer to retrieve payment information regarding their account and to make payments in a few effortless steps.</div></div>
    <div class="abs service" style="top:185px"><div class="service-name">Pack Files</div><div class="service-desc">Payments that are made online using the billing portal/website or via telephone which can be made by check or credit card/debit card payments.</div></div>
    <div class="abs service" style="top:226px"><div class="service-name">kReceivables</div><div class="service-desc">Payments that are made by a customer using online banking or payments made at one of their local payment outlets that accepts utility payments, such as Marvista, Grocemart, HillTop etc.</div></div>
    <div class="abs service" style="top:263px"><div class="service-name">Recurring ACH/<br>Credit Cards</div><div class="service-desc" style="padding-top:9px">Customers that sign up for this service will have funds drafted from their bank account or applied to their credit card each month based on their current balance and they will not have to worry about manually making payments each month or forgetting to make a payment.</div></div>
    <div class="abs service" style="top:327px"><div class="service-name">Billing</div><div class="service-desc">MBA will process billing statements each month based on the guidance of the operator.&nbsp; Bills are automatically calculated based on meter reads and the rate ordinance that was provided by the operator for each of its districts.</div></div>
    <div class="abs service" style="top:377px"><div class="service-name">Secured<br>file storage<br>of payments</div><div class="service-desc" style="padding-top:10px">Every payment that is processed by MBA is stored electronically for a minimum of 2 years and can be accessed for clients upon written request.</div></div>
    <div class="abs service" style="top:438px"><div class="service-name">Research</div><div class="service-desc">MBA provides general to complex research of payments, discrepancies, etc.</div></div>
    <div class="abs service" style="top:464px"><div class="service-name">Support</div><div class="service-desc">MBA provides general support for our clients and if MBA cannot immediately resolve an issue that issue will be escalated to the next higher support level for resolution.</div></div>

    <h2 class="abs section-title" style="top:513px">Advantages of using MBA</h2>
    <div class="abs section-rule" style="top:537px"></div>

    <div class="abs advantages">
      <ol class="adv-list" style="left:11px;width:278px">
        <li style="margin-bottom:9px"><span class="num">1.</span><span>No learning curves to learn software.&nbsp; Payments and billing will be up and running immediately after conversion</span></li>
        <li style="margin-bottom:11px"><span class="num">2.</span><span>Actual staff personnel to talk to when you have an issue.</span></li>
        <li style="margin-bottom:11px"><span class="num">3.</span><span>We have an efficient and experienced team working with a vast understanding of the various tasks involved in finalizing the billing cycle.</span></li>
        <li style="margin-bottom:14px"><span class="num">4.</span><span>Generally, more cost effective than processing payments and billing in-house.</span></li>
        <li><span class="num">5.</span><span>Deposits are usually made faster when using the MBA department versus using in-house processors.</span></li>
      </ol>
      <div class="abs adv-divider"></div>
      <ol class="adv-list" style="left:316px;width:272px">
        <li style="margin-bottom:11px"><span class="num">6.</span><span>Assistance with delinquent letters and tags if requested</span></li>
        <li style="margin-bottom:9px"><span class="num">7.</span><span>Reports to help balance bank statements.</span></li>
        <li style="margin-bottom:10px"><span class="num">8.</span><span>All payments are checked and balanced:
          <ul>
            <li>To make sure that the amount expected to be processed was processed.</li>
            <li>What was expected to go to the bank is what went to the bank.</li>
            <li>And that the bank received each payment.</li>
          </ul></span></li>
        <li><span class="num">9.</span><span>Can provide customizable services depending on our client’s needs.</span></li>
      </ol>
    </div>

    <div class="abs back-footer">
      <span><svg><use href="#icon-phone"/></svg>855.412.0937</span>
      <span><svg><use href="#icon-globe"/></svg>www.kltqe.example</span>
      <span><svg><use href="#icon-pin"/></svg>48715 Brisbow Lane, Houston, TX 77052</span>
    </div>
    <div class="abs bottom-bar"></div>
  </section>
</div>
</body>
</html>
```